Lumen Forge Unique Marketing Website Design

I am starting a new company that is a thought leader in the marketing consulting space. The company is called Lumen Forge. We intend to build a Wordpress site on the Astra Theme with the Spectra builder. Our goal is to become the leading voice that empowers high-ticket service business leaders to become Lumen Forge by equipping them with the cutting-edge frameworks and decision grade intelligence taught in leading business schools. What we are looking for is a website design that is clean and professional, making some use of white space well also being eye catching and distinctive in the consulting space. We will probably want to have a video on the homepage not in the hero section, but just below to explain the company and what we do. Our tagline is "Be found. Be chosen." I have attached a brand guide with some messaging, our typography choices, and our color system. The full site will have a primary nav that is four pages - About us, Services, Insights (essentially a blog), and Contact Us. The goal of this project is to develop an art direction that I can give to a designer to build loads of new pages.

Target Market(s)

Business owners (mostly male) from 30-60 years old, looking to fix their sales and marketing funnel.

Industry/Entity Type

Marketing consulting

Font styles to use
Sans Serif

Requirements
Must have
• A clean, professional design that builds trust with owners of high-ticket service businesses. We need a space for explainer video, and sections that tell prospects what we do. Would also like to have a blog carousel.
Nice to have
• Social feeds, if possible. See attached documents for colors and fonts.
Should not have
• Our feel is professional enough to be trustworthy, but unique enough to be memorable. Cartoon ideas do not meet the professional test, and we do not want the website to appear feminine.

```html
<!DOCTYPE html>
<html lang="en">
<head>
<meta charset="utf-8">
<title>Lumen Forge — Be Found. Be Chosen.</title>
<link href="https://fonts.googleapis.com/css2?family=Oswald:wght@500;600&family=Poppins:wght@400;500;600&display=swap" rel="stylesheet">
<style>
:root{
  --navy:#1b2130;
  --navy-deep:#171d2a;
  --blue:#1a6fe0;
  --blue-title:#2170dc;
  --ink:#222630;
  --muted:#5c6270;
  --soft:#9aa0ab;
  --charcoal:#353535;
  --green:#1fbd84;
  --pale:#f1f6fc;
  --mist:#e9eef5;
  --white:#ffffff;
}
*{margin:0;padding:0;box-sizing:border-box}
html,body{width:1200px;height:3834px;overflow:hidden}
body{position:relative;background:var(--white);font-family:'Poppins',sans-serif;color:var(--ink)}
.abs{position:absolute}
.display{font-family:'Oswald',sans-serif;font-weight:600;letter-spacing:.2px}
.accent{color:var(--blue-title)}
.btn{position:absolute;background:var(--blue);color:var(--white);font-size:12px;display:flex;align-items:center;justify-content:center;border-radius:2px}
.photo{position:absolute}
.brand{display:flex;align-items:center;gap:8px;font-family:'Poppins',sans-serif;font-weight:600;color:var(--navy);letter-spacing:.3px}
.brand .mark{width:12px;height:12px;background:var(--blue)}

/* header */
.site-header{left:0;top:0;width:1200px;height:86px;background:var(--navy)}
.header-logo{left:74px;top:27px;width:165px;height:30px;background:var(--white);justify-content:center;font-size:15px}
.nav-frame{left:390px;top:0;width:810px;height:86px;border-left:1px solid #3a4152}
.nav-row{left:390px;top:0;width:690px;height:43px;border-bottom:1px solid #3a4152}
.nav-item{position:absolute;top:15px;color:var(--white);font-size:11px;transform:translateX(-50%)}
.nav-sep{position:absolute;top:0;width:1px;height:43px;background:#3a4152}
.socials{left:1058px;top:10px;display:flex;gap:6px}
.socials span{width:17px;height:17px;border-radius:50%;background:var(--white)}
.info{top:57px;font-size:10px;color:var(--white)}
.info b{font-weight:400;color:#3d8bf0}
.bar{top:56px;width:2px;height:14px;background:#8a92a3}

/* hero */
.hero{left:0;top:86px;width:1200px;height:405px;background:linear-gradient(100deg,#33445e 0%,#4d6380 45%,#6b7f97 75%,#3f516b 100%)}
.hero-shade{left:0;top:86px;width:1200px;height:405px;background:rgba(20,34,58,.45)}
.hero-title{left:231px;top:150px;color:var(--white);font-family:'Oswald',sans-serif;font-weight:600;font-size:88px;line-height:74px;letter-spacing:-1px}
.hero-sub{left:234px;top:314px;color:var(--white);font-size:11px;line-height:14px;width:420px}
.arrow{top:270px}

/* about */
.h-sec{font-size:34px;line-height:39px;color:var(--ink)}
.about-title{left:234px;top:614px}
.p{font-size:11px;line-height:16px;color:var(--muted)}
.about-p1{left:234px;top:700px;width:292px}
.about-p2{left:234px;top:782px;width:292px}
.about-photo{left:666px;top:551px;width:299px;height:354px;background:linear-gradient(140deg,#8fa6bf 0%,#d2dbe6 40%,#7f93aa 70%,#c9d3df 100%)}
.play{left:792px;top:697px;width:60px;height:60px;border-radius:50%;background:rgba(255,255,255,.85);display:flex;align-items:center;justify-content:center}
.about-card{left:596px;top:807px;width:166px;height:134px;background:var(--white);border:1px solid #e1e4ea;justify-content:center;font-size:16px}

/* section headings */
.centered{left:0;width:1200px;text-align:center}
.sec-title{font-size:34px;line-height:40px}
.sec-sub{font-size:10.5px;line-height:14px;color:var(--muted)}

/* services */
.service{position:absolute;top:1102px;width:230px;height:295px;background:var(--white);box-shadow:0 4px 18px rgba(30,40,60,.10)}
.service .photo{left:13px;top:0;width:204px;height:240px}
.service p{position:absolute;left:0;width:230px;top:258px;text-align:center;font-size:13.5px;font-weight:500;color:var(--ink)}
.chev{top:1234px}

/* who we are */
.who-photo{left:0;top:1516px;width:599px;height:330px;background:linear-gradient(110deg,#d7d2c8 0%,#b7a89a 40%,#e4e2dc 65%,#9b8a7a 100%)}
.who-panel{left:599px;top:1516px;width:601px;height:330px;background:var(--charcoal)}
.who-title{left:634px;top:1548px;color:var(--white);font-size:32px}
.who-text{left:634px;top:1606px;width:386px;font-size:11px;line-height:15px;color:#e8e8e8}

/* team */
.team-band{left:0;top:1846px;width:1200px;height:484px;background:var(--pale)}
.member{position:absolute;top:2004px;width:165px;height:232px;background:var(--white);box-shadow:0 2px 10px rgba(30,40,60,.06)}
.member .photo{left:0;top:0;width:165px;height:176px}
.member .name{position:absolute;left:18px;top:191px;font-size:11px;color:var(--ink)}
.member .role{position:absolute;left:18px;top:207px;font-size:9px;color:var(--soft)}

/* blog */
.blog-photo{position:absolute}
.post{position:absolute;padding:22px 22px 0 22px}
.post h3{font-size:14px;line-height:20px;font-weight:500}
.post .excerpt{font-size:10px;line-height:16px;margin-top:8px}
.post .meta{margin-top:12px;padding-top:10px;font-size:9px;letter-spacing:.6px;line-height:13px}
.post-light{left:235px;top:2624px;width:215px;height:183px;background:var(--white);box-shadow:0 4px 16px rgba(30,40,60,.12);padding:18px 18px 0 20px}
.post-light h3{color:var(--ink)}
.post-light .excerpt{color:var(--soft)}
.post-light .meta{border-top:1px solid #eef0f4;color:var(--blue)}
.post-light .meta span{display:block;color:var(--muted)}
.post-green{left:735px;top:2485px;width:230px;height:227px;background:var(--green);color:var(--white)}
.post-blue{left:485px;top:2729px;width:230px;height:227px;background:var(--blue);color:var(--white)}
.post-green .excerpt,.post-blue .excerpt{color:rgba(255,255,255,.9)}
.post-green .meta,.post-blue .meta{border-top:1px solid rgba(255,255,255,.7)}

/* contact */
.contact-band{left:0;top:3075px;width:1200px;height:506px;background:linear-gradient(180deg,#e9eef5 0%,#eef2f7 70%,#dfe5ec 100%)}
.skyline{left:0;top:3460px;width:1200px;height:121px;background:linear-gradient(180deg,rgba(233,238,245,0) 0%,#b9c3cf 55%,#8d99a8 100%)}
.field{position:absolute;background:var(--white);border:1px solid #dde3ea;display:flex;align-items:flex-start;padding:14px 14px;font-size:9.5px;color:#8a909b;gap:8px}
.field svg{flex:none}

/* footer */
.site-footer{left:0;top:3581px;width:1200px;height:253px;background:var(--navy-deep)}
.footer-logo{left:234px;top:3635px;width:173px;height:31px;background:var(--white);justify-content:center;font-size:16px}
.footer-text{left:234px;top:3686px;width:282px;font-size:8.5px;line-height:11px;color:#d4d7de}
.f-head{left:566px;top:3620px;color:var(--white);font-size:15px}
.f-link{position:absolute;color:var(--white);font-size:10px}
.f-small{color:#aeb4bf;font-size:8.5px}
.f-big{color:var(--white);font-size:15px;font-weight:600}
.f-mail{color:var(--white);font-size:12.5px;font-weight:600}
.f-icons{left:745px;top:3757px;display:flex;gap:12px}
.f-icons span{width:11px;height:11px;border-radius:50%;background:#c6cbd4}
.copyright{left:0;top:3809px;width:1200px;text-align:center;font-size:9px;color:#c2c6cf}
</style>
</head>
<body>

<!-- Header -->
<header class="abs site-header">
  <div class="abs brand header-logo"><span class="mark"></span>LUMEN FORGE</div>
  <div class="abs nav-frame"></div>
  <div class="abs nav-row">
    <span class="nav-item" style="left:63px">HOME</span>
    <span class="nav-item" style="left:194px">ABOUT US</span>
    <span class="nav-item" style="left:332px">SERVICES</span>
    <span class="nav-item" style="left:460px">BLOG</span>
    <span class="nav-item" style="left:594px">CONTACT US</span>
  </div>
  <div class="abs socials"><span></span><span></span><span></span></div>
  <div class="abs info" style="left:435px"><b>Email:</b> hello@lumenforge.co</div>
  <div class="abs bar" style="left:659px"></div>
  <div class="abs info" style="left:725px"><b>Call:</b> +1 555 0142 300</div>
  <div class="abs bar" style="left:877px"></div>
  <div class="abs info" style="left:936px"><b>Opening:</b> Monday - Friday (8AM - 9PM)</div>
</header>

<!-- Hero -->
<section>
  <div class="abs hero" role="img" aria-label="Business team smiling around a meeting table in a bright office"></div>
  <div class="abs hero-shade"></div>
  <svg class="abs arrow" style="left:24px" width="18" height="34" viewBox="0 0 18 34"><path d="M16 2 2 17l14 15" fill="none" stroke="#fff" stroke-width="1.6"/></svg>
  <svg class="abs arrow" style="left:1158px" width="18" height="34" viewBox="0 0 18 34"><path d="M2 2l14 15L2 32" fill="none" stroke="#fff" stroke-width="1.6"/></svg>
  <h1 class="abs hero-title">Be Found.<br>Be Chosen.</h1>
  <p class="abs hero-sub">We aim to make the process easy for you! We will find home health and take care of coordinating all care needed for your patient.</p>
  <div class="btn" style="left:234px;top:359px;width:149px;height:36px;font-size:10px;font-weight:500;letter-spacing:.4px">EXPLORE SERVICES</div>
</section>

<!-- About -->
<section>
  <h2 class="abs display h-sec about-title">About Us<br><span class="accent">Lumen Forge</span></h2>
  <p class="abs p about-p1">Every pleasure is to be welcomed and every pain avoided. But in certain circumstances and owing to the claims of duty obligations of business it will frequently occur that.</p>
  <p class="abs p about-p2">If you're able to become pregnant, you should use effective and reliable birth control while taking a GLP-1 agonist. If you become pregnant while taking the immediately.</p>
  <div class="btn" style="left:235px;top:865px;width:103px;height:31px;font-size:11px">Learn More</div>
  <div class="photo about-photo" role="img" aria-label="Explainer video still: two consultants in a meeting over printed charts"></div>
  <div class="abs play"><svg width="22" height="24" viewBox="0 0 22 24"><path d="M3 2l17 10L3 22z" fill="#1a6fe0"/></svg></div>
  <div class="abs brand about-card"><span class="mark"></span>LUMEN FORGE</div>
</section>

<!-- Services -->
<section>
  <h2 class="abs display centered sec-title" style="top:982px">Our <span class="accent">Services</span></h2>
  <p class="abs centered sec-sub" style="top:1040px">The Most Eminent Visas and Immigration Consultant service provider.<br>Branches in India and overseas.</p>
  <svg class="abs chev" style="left:193px" width="10" height="18" viewBox="0 0 10 18"><path d="M9 1 1 9l8 8" fill="none" stroke="#9aa0ab" stroke-width="1.3"/></svg>
  <svg class="abs chev" style="left:997px" width="10" height="18" viewBox="0 0 10 18"><path d="M1 1l8 8-8 8" fill="none" stroke="#9aa0ab" stroke-width="1.3"/></svg>
  <div class="service" style="left:235px"><div class="photo" role="img" aria-label="Two consultants reviewing documents at a desk" style="background:linear-gradient(160deg,#c9d2dc,#5a6678 60%,#2f3846)"></div><p>Revenue Intelligence</p></div>
  <div class="service" style="left:485px"><div class="photo" role="img" aria-label="Business handshake over a laptop" style="background:linear-gradient(160deg,#b8c0cb,#3c4a60 55%,#c7ccd3)"></div><p>Revenue Psychology</p></div>
  <div class="service" style="left:735px"><div class="photo" role="img" aria-label="Two professionals reviewing a tablet" style="background:linear-gradient(160deg,#d9d6d0,#8a6a50 45%,#2c2f36)"></div><p>Demand Architecture</p></div>
  <div class="btn" style="left:536px;top:1435px;width:128px;height:30px;font-size:11px">View All Services</div>
</section>

<!-- Who We Are -->
<section>
  <div class="photo who-photo" role="img" aria-label="Team gathered around a long table in a bright loft office"></div>
  <div class="abs who-panel"></div>
  <h2 class="abs display who-title">Who We Are</h2>
  <p class="abs who-text">It is a long established fact that a reader will be distracted by the readable content of a page when looking at its layout. The point of using Lorem Ipsum is that it has a more-or-less normal distribution of letters, as opposed to using 'Content here, content here', making it look like readable English. Many desktop publishing packages and web page editors now use Lorem Ipsum as their default model text, and a search for 'lorem ipsum' will uncover many web sites still in their infancy. Various versions have evolved over the years, sometimes by accident, sometimes on purpose (injected humour and the like.</p>
  <div class="btn" style="left:636px;top:1776px;width:114px;height:32px;font-size:11px">Learn More</div>
</section>

<!-- Team -->
<section>
  <div class="abs team-band"></div>
  <h2 class="abs display centered sec-title" style="top:1893px">Meet Our <span class="accent">Team</span></h2>
  <p class="abs centered sec-sub" style="top:1943px">The Most Eminent Visas and Immigration Consultant service provider.<br>Branches in India and overseas.</p>
  <div class="member" style="left:244px"><div class="photo" role="img" aria-label="Portrait of a team member" style="background:linear-gradient(180deg,#e7e7e7,#8d8f94)"></div><span class="name">Daniel Reyes</span><span class="role">Migration Agent</span></div>
  <div class="member" style="left:427px"><div class="photo" role="img" aria-label="Portrait of a team member in a suit" style="background:linear-gradient(180deg,#d6d6d4,#3e4450)"></div><span class="name">Owen Carter</span><span class="role">Migration Agent</span></div>
  <div class="member" style="left:610px"><div class="photo" role="img" aria-label="Portrait of a team member in a blue shirt" style="background:linear-gradient(180deg,#e2e2e2,#5f7fa6)"></div><span class="name">Marcus Hale</span><span class="role">Migration Agent</span></div>
  <div class="member" style="left:794px"><div class="photo" role="img" aria-label="Portrait of a team member in a blazer" style="background:linear-gradient(180deg,#dcdcdc,#3a3a40)"></div><span class="name">Claire Benton</span><span class="role">Migration Agent</span></div>
  <div class="btn" style="left:544px;top:2269px;width:115px;height:30px;font-size:11px">View All</div>
</section>

<!-- Blog -->
<section>
  <h2 class="abs display centered sec-title" style="top:2374px">Latest <span class="accent">Blog</span></h2>
  <p class="abs centered sec-sub" style="top:2423px">The Most Eminent Visas and Immigration Consultant service provider.<br>Branches in India and overseas.</p>

  <div class="blog-photo" role="img" aria-label="Two colleagues talking by an office window" style="left:235px;top:2485px;width:230px;height:171px;background:linear-gradient(150deg,#e4e7ea,#6d7784 55%,#2d333d)"></div>
  <article class="post post-light">
    <h3>Operational Management and Strategic Planning</h3>
    <p class="excerpt">Consectetuer fringilla aenean sagittis potenti ullamcorper nam porta feugiat. Ante urna congue feugiat efficitur vel duis.</p>
    <p class="meta">VIRTUAL ASSISTANT<span>Jan 02, 2024</span></p>
  </article>
  <div class="blog-photo" role="img" aria-label="Presenter at a whiteboard with colleagues" style="left:235px;top:2823px;width:230px;height:133px;background:linear-gradient(120deg,#e8e8e6,#8c7a68 50%,#3b3f48)"></div>

  <div class="blog-photo" role="img" aria-label="Woman working at a desk with a laptop" style="left:485px;top:2485px;width:230px;height:227px;background:linear-gradient(150deg,#d9d2c8,#a88e74 50%,#5b5f66)"></div>
  <article class="post post-blue">
    <h3>Do you Prefer an Online Time and Attendacne Solution?</h3>
    <p class="excerpt">Consectetuer fringilla aenean sagittis potenti ullamcorper nam porta feugiat. Ante urna congue feugiat efficitur vel duis.</p>
    <p class="meta">VIRTUAL ASSISTANT<br>Jan 02, 2024</p>
  </article>

  <article class="post post-green">
    <h3>Regional Manager &amp; limited time management.</h3>
    <p class="excerpt">Consectetuer fringilla aenean sagittis potenti ullamcorper nam porta feugiat. Ante urna congue feugiat efficitur vel duis.</p>
    <p class="meta">VIRTUAL ASSISTANT<br>Jan 02, 2024</p>
  </article>
  <div class="blog-photo" role="img" aria-label="Team meeting around a table in front of a world map" style="left:735px;top:2729px;width:230px;height:227px;background:linear-gradient(150deg,#c9c6c0,#6d6660 50%,#2f3137)"></div>

  <div class="btn" style="left:539px;top:2994px;width:122px;height:30px;font-size:11px">View More News</div>
</section>

<!-- Contact -->
<section>
  <div class="abs contact-band"></div>
  <div class="abs skyline" role="img" aria-label="City skyline rising above low clouds"></div>
  <h2 class="abs display centered sec-title" style="top:3101px">Contact <span class="accent">Now</span></h2>
  <p class="abs centered sec-sub" style="top:3154px;font-size:9.5px">The actuaries at Harrow Lane have provided consulting services to over 300</p>

  <div class="field" style="left:325px;top:3189px;width:266px;height:38px">
    <svg width="10" height="10" viewBox="0 0 10 10"><circle cx="5" cy="3" r="2.2" fill="none" stroke="#8a909b"/><path d="M1 10c0-3 8-3 8 0" fill="none" stroke="#8a909b"/></svg>First Name</div>
  <div class="field" style="left:606px;top:3189px;width:267px;height:38px">
    <svg width="10" height="10" viewBox="0 0 10 10"><circle cx="5" cy="3" r="2.2" fill="none" stroke="#8a909b"/><path d="M1 10c0-3 8-3 8 0" fill="none" stroke="#8a909b"/></svg>Last Name</div>
  <div class="field" style="left:325px;top:3240px;width:266px;height:37px">
    <svg width="10" height="10" viewBox="0 0 10 10"><path d="M2 1l2 2-1 1.5c.8 1.5 1.8 2.5 3.3 3.3L7.8 6.8l2 2L8.5 10C4.5 9.5.5 5.5 0 1.5z" fill="none" stroke="#8a909b" stroke-width=".9"/></svg>Email</div>
  <div class="field" style="left:606px;top:3240px;width:267px;height:37px">
    <svg width="10" height="10" viewBox="0 0 10 10"><path d="M5 9.5S1.5 6 1.5 3.8a3.5 3.5 0 0 1 7 0C8.5 6 5 9.5 5 9.5z" fill="none" stroke="#8a909b"/><circle cx="5" cy="3.8" r="1.1" fill="#8a909b"/></svg>Address</div>
  <div class="field" style="left:325px;top:3289px;width:548px;height:124px">
    <svg width="10" height="10" viewBox="0 0 10 10"><path d="M1 2h8v5H4l-2 2V7H1z" fill="none" stroke="#8a909b" stroke-width=".9"/></svg>Message</div>
  <div class="btn" style="left:539px;top:3444px;width:121px;height:30px;font-size:10px;font-weight:500">SUBMIT NOW</div>
</section>

<!-- Footer -->
<footer>
  <div class="abs site-footer"></div>
  <div class="abs brand footer-logo"><span class="mark"></span>LUMEN FORGE</div>
  <p class="abs footer-text">It is a long established fact that a reader will be distracted by the readable content of a page when looking at its layout. The point of using Lorem Ipsum is that it has a more-or-less normal distribution of letters, as opposed to using 'Content here, content here', making it look like readable English.</p>
  <h4 class="abs f-head" style="font-weight:500">Quick Links</h4>
  <span class="f-link" style="left:566px;top:3660px">Home</span>
  <span class="f-link" style="left:633px;top:3660px">Blog</span>
  <span class="f-link" style="left:566px;top:3698px">About Us</span>
  <span class="f-link" style="left:633px;top:3698px">Contact Us</span>
  <span class="f-link" style="left:566px;top:3736px">Services</span>
  <span class="abs f-small" style="left:745px;top:3618px">Have Any Question?</span>
  <span class="abs f-big" style="left:745px;top:3632px">+1 555 0148 220</span>
  <span class="abs f-small" style="left:745px;top:3664px">Our Mailbox</span>
  <span class="abs f-mail" style="left:745px;top:3680px">studio@lumenforge.co</span>
  <span class="abs f-small" style="left:745px;top:3732px">Social Links</span>
  <div class="abs f-icons"><span></span><span></span><span></span></div>
  <p class="abs copyright">Copyright © 2026 lumenforge · All Rights Reserved.</p>
</footer>

</body>
</html>
```